Willowmere Recovery Brochure

We need a brochure template we can change photo's and words at a later date. WE offer rehabilitation to injured horses and ponies.
Either use our Willowmere Grounds or Willowmere Recovery logo but not both. A strong preference for the horse being led to feature first.

Target Market(s)

Horse Owners

Font styles to use
Serif

Colors
f78f20

Requirements
Must have
• Ability to write the text and interchange photos within the layout at a later date.
Nice to have
• Our colours are orange and black

```html
<!DOCTYPE html>
<html lang="en">
<head>
<meta charset="utf-8">
<title>Willowmere Recovery Brochure</title>
<link href="https://fonts.googleapis.com/css2?family=Montserrat:wght@400;600;700;800&family=Noto+Serif:wght@400;700&display=swap" rel="stylesheet">
<style>
  :root{
    --orange:#f78f20;
    --orange-soft:rgba(247,143,32,.86);
    --ink:#1c1c1c;
    --text:#4a4a4a;
    --paper:#ffffff;
    --backdrop:#ececec;
  }
  *{box-sizing:border-box;margin:0;padding:0}
  html,body{width:678px;height:1200px;overflow:hidden;background:var(--backdrop)}
  body{position:relative;font-family:'Montserrat',sans-serif;color:var(--text)}
  .spread{position:absolute;left:29px;width:601px;height:465px;background:var(--paper);
    transform:scale(1.0316);transform-origin:0 0;box-shadow:0 4px 14px rgba(0,0,0,.18);overflow:hidden}
  .spread--outside{top:80px}
  .spread--inside{top:640px}
  .abs{position:absolute}
  .band{left:0;top:78px;width:596px;height:135px;background:var(--orange)}
  .photo{border:3px solid var(--paper)}
  .photo--stable{left:11px;top:22px;width:163px;height:163px;background:linear-gradient(135deg,#2f2a24 0%,#6b4424 45%,#a0632e 65%,#c9a46a 100%)}
  .photo--led{left:410px;top:150px;width:177px;height:271px;background:linear-gradient(180deg,#4f6b3a 0%,#7e8f57 35%,#9a6a3e 60%,#c9bda8 100%)}
  .photo--grazing{left:81px;top:40px;width:335px;height:386px;border:none;background:linear-gradient(180deg,#3f4a2e 0%,#6e5a3a 35%,#8a4f2a 55%,#7b7f4a 80%,#9a9a6a 100%)}
  .brand{display:flex;align-items:center;gap:4px;font-family:'Noto Serif',serif;font-size:10px;color:var(--ink);white-space:nowrap}
  .brand__mark{width:14px;height:14px;background:var(--ink)}
  .heading{font-weight:700;letter-spacing:.5px;color:var(--ink);font-size:13px}
  .heading--light{color:var(--paper);font-size:12.5px;text-align:center}
  .heading--orange{color:var(--orange);font-size:15px}
  .heading--big{color:var(--paper);font-size:25px;font-weight:800}
  .rule{width:14px;height:2px;background:var(--ink)}
  .sub{color:var(--orange);font-weight:700;font-size:7.5px}
  .body{font-size:4.6px;line-height:1.45;text-align:justify}
  .body p+p{margin-top:4px}
  .body--light{color:var(--paper);text-align:center}
  .body--about{color:var(--paper);font-size:5.3px}
  .body--rehab{font-size:5.4px;color:var(--ink)}
  .contact{left:210px;width:190px;text-align:center;color:var(--ink)}
  .icon{width:16px;height:16px;margin:0 auto}
  .contact__line{font-size:7px;font-weight:600;margin-top:6px}
  .contact__line--small{font-size:5.2px}
  .title-kicker{display:flex;align-items:center;justify-content:center;gap:4px;font-family:'Noto Serif',serif;font-weight:700;color:var(--ink);font-size:11px}
  .title-kicker span{display:block;width:18px;height:1px;background:var(--ink)}
  .title-main{font-family:'Noto Serif',serif;font-weight:700;color:var(--paper);font-size:21px;text-align:center}
  .url{font-size:6.5px;font-weight:600;color:var(--ink);text-align:center}
  .about-box{left:12px;top:73px;width:179px;height:324px;background:var(--orange-soft);padding:22px 14px}
</style>
</head>
<body>

<section class="spread spread--outside" aria-label="Brochure outside spread">
  <div class="abs band"></div>

  <!-- Left panel: adopted -->
  <div class="abs photo photo--stable" role="img" aria-label="Photo of a chestnut horse looking out of a stable door"></div>
  <div class="abs" style="left:20px;top:224px;width:163px">
    <h2 class="heading">ADOPTED</h2>
    <div class="rule" style="width:3px;height:3px;border-radius:50%;margin:3px 0 5px"></div>
    <div class="body"><p>At Willowmere Equine Sanctuary we take time with our horses to make sure we can find their "Furever" home. These lucky horses have found their humans and are currently adopted.</p></div>
    <h3 class="sub" style="margin:9px 0 6px">JIMMY – ADOPTED</h3>
    <div class="body"><p>Little Jimmy has just been weaned and has commenced his basic ground work education. Jimmy was part of a large seizure early in 2016 – 100 starving unhandled horses were brought to WES for rehabilitation. We love little Jimmy – he's very sweet. Here he can be seen on his walk meeting other WES ...</p></div>
    <h3 class="sub" style="margin:9px 0 6px">FLYNN – ADOPTED</h3>
    <div class="body">
      <p>Its not hard to see why Flynn was a fav at the sale that day – including a beautiful heart on his forehead.</p>
      <p>However the only interest was the doggers – he was purchased and surrendered to WES. We assessed him under saddle and he soon caught the eye of Harriet – who had recently adopted Joey.</p>
      <p>Needless to say he was soon adopted by Harriet! Now called Frank</p>
    </div>
  </div>

  <!-- Middle panel: sponsorship + contact -->
  <div class="abs" style="left:210px;top:95px;width:186px">
    <h2 class="heading heading--light">SPONSORSHIP</h2>
    <div class="rule" style="width:3px;height:3px;border-radius:50%;background:#fff;margin:3px auto 7px"></div>
    <div class="body body--light">
      <p>At Willowmere Equine Sanctuary, we have a number of our animals available for Sponsorship. The majority are horses or ponies reflecting our focus however from time to time the odd farm animal finds itself needing the peace of our Sanctuary.</p>
      <p>Generally, this means that the horse requires long-term rehabilitation including ongoing vet care etc as more often than not, the horse will have arrived in poor condition.</p>
      <p>Your sponsorship donation enables the Sanctuary to continue caring with all rehabilitation and ongoing lifetime costs for the horse ensuring a healthy, happy outcome.</p>
    </div>
  </div>
  <div class="abs contact" style="top:250px">
    <div class="brand" style="justify-content:center"><span class="brand__mark"></span>Willowmere Recovery</div>
    <svg class="icon" style="margin-top:22px" viewBox="0 0 16 16"><circle cx="8" cy="8" r="7.5" fill="none" stroke="#f78f20" stroke-width=".8"/><path d="M5.5 4.5l1.5 0 .7 2-1 .8c.5 1 1.2 1.7 2.2 2.2l.8-1 2 .7v1.5c0 .5-.5.8-1 .8C7.6 11.3 4.7 8.4 4.7 5.3c0-.5.3-.8.8-.8z" fill="#f78f20"/></svg>
    <p class="contact__line">0400 123 456</p>
    <svg class="icon" style="margin-top:11px" viewBox="0 0 16 16"><circle cx="8" cy="8" r="7.5" fill="none" stroke="#f78f20" stroke-width=".8"/><rect x="4.5" y="5.5" width="7" height="5" fill="none" stroke="#f78f20" stroke-width=".8"/><path d="M4.5 5.5l3.5 3 3.5-3" fill="none" stroke="#f78f20" stroke-width=".8"/></svg>
    <p class="contact__line contact__line--small">hello@willowmere.org.au</p>
    <svg class="icon" style="margin-top:11px" viewBox="0 0 16 16"><circle cx="8" cy="8" r="7.5" fill="none" stroke="#f78f20" stroke-width=".8"/><circle cx="8" cy="8" r="3.5" fill="none" stroke="#f78f20" stroke-width=".8"/><path d="M4.5 8h7M8 4.5c-1.5 2-1.5 5 0 7M8 4.5c1.5 2 1.5 5 0 7" fill="none" stroke="#f78f20" stroke-width=".6"/></svg>
    <p class="contact__line contact__line--small">www.willowmere.org.au</p>
  </div>

  <!-- Right panel: cover -->
  <div class="abs brand" style="left:452px;top:36px"><span class="brand__mark"></span>Willowmere Recovery</div>
  <div class="abs" style="left:408px;top:93px;width:193px">
    <div class="title-kicker"><span></span>Willowmere<span></span></div>
    <div class="title-main">Recovery</div>
  </div>
  <div class="abs photo photo--led" role="img" aria-label="Photo of a handler leading a chestnut horse along a path with a small dog"></div>
  <p class="abs url" style="left:408px;top:435px;width:193px">www.willowmere.org.au</p>
</section>

<section class="spread spread--inside" aria-label="Brochure inside spread">
  <div class="abs photo photo--grazing" role="img" aria-label="Photo of a bay horse grazing in a paddock"></div>
  <div class="abs about-box">
    <h2 class="heading heading--big">ABOUT US</h2>
    <div class="body body--about" style="margin-top:18px">
      <p>Willowmere Equine Sanctuary (WES) was founded by passionate animal lovers and advocates in 2014, in response to an ever-increasing number of horses passing through the saleyards, and into the hands of knackeries.</p>
      <p style="margin-top:7px">The name was selected to pay homage to the brilliant protective work done by the Sea Wardens, and to reflect our mission of providing sanctuary and solace to unwanted, injured, and otherwise vulnerable horses and ponies. We are a fully registered charity on the national charities register, and rely largely on funding from committee members, and a small number of sponsors, to continue our work.</p>
      <p style="margin-top:7px">Last year (2016) has been one of tremendous growth for WES, commencing with the move to our new, 200 acre Sanctuary in Ashby Vale. This was promptly followed by the arrival of 113 horses as part of the largest state welfare authority horse seizure in our history.</p>
    </div>
  </div>
  <div class="abs" style="left:433px;top:100px;width:136px">
    <h2 class="heading heading--orange">REHABILITATION</h2>
    <div class="rule" style="margin:9px auto 20px"></div>
    <div class="body body--rehab">
      <p>Horses that first come to the Sanctuary are given time to unwind, relax and in turn, be assessed for rehabilitation needs.</p>
      <p style="margin-top:7px">Each horse will always have its own specific needs addressed and for us, there is no rush. Taking time to learn more about each horse allows us to better assess them for adoption suitability. We take the worry out of purchasing an 'unknown' horse for you.</p>
      <p style="margin-top:16px">Your ongoing support of donations enables us to continue saving and rehabilitating horses giving them a second chance in life.</p>
      <p style="margin-top:7px;text-align:left">Northbank<br>Willowmere Equine Sanctuary<br>BSB: 000 111<br>ACC: 123456789</p>
      <p style="margin-top:7px">Listed below are our current horses under rehabilitation – we welcome expressions of interest .</p>
    </div>
  </div>
</section>

</body>
</html>
```